VENTURE CAPITAL GROUP BUSINESS CARD DESIGN

Venture Capital Group based in SF looking for a bold business card design. No trendy colour explosion, 3D effects etc. Just "simple" optical effects. Works on your brain, keeps your eye focused and sticks to your mind.
Target Market(s)
Technology startups
Industry/Entity Type
Venture Capital
Contact Information for Business Card
BARNABY WHITLOCK
MANAGING PARTNER
817 FERN ST SAN FRANCISCO, CA 94111
415.555.0143 O
415.555.0167 F
415.555.0192 C
barn@halcyonridgefund.example

```html
<!DOCTYPE html>
<html lang="en">
<head>
<meta charset="utf-8">
<title>Halcyon Ridge Fund – Business Card</title>
<link rel="stylesheet" href="https://fonts.googleapis.com/css2?family=Open+Sans:ital,wght@0,400;0,600;1,400&family=Arimo:wght@400;700&display=swap">
<style>
  :root {
    --page-bg: #eef1ee;
    --card-white: #ffffff;
    --green-deep: #137a0c;
    --green-text: #1a7a12;
    --green-bright: #3fc22b;
    --green-mid: #25a617;
    --pattern-grey-a: #e9ecea;
    --pattern-grey-b: #ffffff;
    --ink-light: #ffffff;
  }
  * { margin: 0; padding: 0; box-sizing: border-box; }
  html, body { width: 995px; height: 1200px; overflow: hidden; }
  body { background: var(--page-bg); position: relative; font-family: "Open Sans", sans-serif; }

  .card { position: absolute; overflow: hidden; box-shadow: 0 6px 14px rgba(0,0,0,.18); }
  .card svg.card-shapes { position: absolute; inset: 0; }

  /* Front */
  .card-front { left: 47px; top: 45px; width: 897px; height: 528px; background: var(--card-white); }
  .holder { position: absolute; left: 80px; top: 124px; width: 389px; text-align: center; color: var(--green-text); white-space: nowrap; }
  .holder-name { font-size: 37px; font-weight: 400; line-height: 1.1; }
  .holder-title { font-size: 33px; font-style: italic; line-height: 1.15; }

  .contact-lines { position: absolute; left: 49px; top: 301px; font-family: "Arimo", sans-serif; font-weight: 700; font-size: 22px; line-height: 29.5px; color: var(--ink-light); white-space: nowrap; }

  .brand { position: absolute; left: 524px; top: 288px; width: 338px; text-align: center; color: var(--green-text); font-weight: 600; font-size: 32px; line-height: 1.12; letter-spacing: 1px; }

  .web-lines { position: absolute; right: 44px; top: 427px; text-align: right; font-family: "Arimo", sans-serif; font-weight: 700; font-size: 24px; line-height: 28px; color: var(--ink-light); white-space: nowrap; }

  /* Back */
  .card-back { left: 49px; top: 606px; width: 893px; height: 524px; }
  .brand-back { position: absolute; left: 332px; top: 158px; width: 270px; text-align: center; color: var(--ink-light); font-weight: 600; font-size: 30px; line-height: 1.12; letter-spacing: 1px; }
  .back-web { position: absolute; left: 0; width: 100%; top: 364px; text-align: center; color: var(--ink-light); font-family: "Arimo", sans-serif; font-size: 34px; line-height: 39px; white-space: nowrap; }
</style>
</head>
<body>

<section class="card card-front">
  <svg class="card-shapes" width="897" height="528" viewBox="0 0 897 528">
    <defs>
      <linearGradient id="faint-pattern" x1="0" y1="0" x2="1" y2="0">
        <stop offset="0" stop-color="var(--pattern-grey-a)"/>
        <stop offset="1" stop-color="var(--pattern-grey-b)"/>
      </linearGradient>
      <radialGradient id="mark-disc" cx=".4" cy=".4" r=".7">
        <stop offset="0" stop-color="#ffffff"/>
        <stop offset="1" stop-color="#d7dcda"/>
      </radialGradient>
      <clipPath id="contact-panel-clip">
        <polygon points="5,271 527,271 291,516 291,446 5,446"/>
      </clipPath>
    </defs>
    <rect x="48" y="47" width="479" height="219" fill="url(#faint-pattern)" role="img" aria-label="Faint grey concentric-ring pattern"/>
    <polygon points="5,271 527,271 291,516 291,446 5,446" fill="var(--green-deep)"/>
    <g clip-path="url(#contact-panel-clip)">
      <rect x="5" y="283" width="520" height="148" fill="var(--green-mid)" opacity=".55" role="img" aria-label="Green concentric-ring pattern"/>
    </g>
    <polygon points="314,512 437,384 894,384 894,512" fill="var(--green-deep)"/>
    <circle cx="719" cy="164" r="100" fill="url(#mark-disc)"/>
  </svg>

  <div class="holder">
    <p class="holder-name">BARNABY WHITLOCK</p>
    <p class="holder-title">Managing Partner</p>
  </div>

  <div class="contact-lines">
    <p>817 Fern st.&nbsp; San francisco, CA 94111</p>
    <p>415.555.0143 O</p>
    <p>415.555.0167 F</p>
    <p>415.555.0192 C</p>
  </div>

  <p class="brand">HALCYON RIDGE<br>FUND</p>

  <div class="web-lines">
    <p>barn@halcyonridgefund.example</p>
    <p>www.halcyonridgefund.example</p>
  </div>
</section>

<section class="card card-back">
  <svg class="card-shapes" width="893" height="524" viewBox="0 0 893 524">
    <defs>
      <linearGradient id="back-pattern" x1="0" y1="0" x2="0" y2="1">
        <stop offset="0" stop-color="var(--green-bright)"/>
        <stop offset="1" stop-color="var(--green-mid)"/>
      </linearGradient>
    </defs>
    <rect width="893" height="524" fill="url(#back-pattern)" role="img" aria-label="Green concentric-ring pattern"/>
    <rect x="45" y="74" width="803" height="282" fill="#ffffff" opacity=".12"/>
    <rect x="0" y="356" width="893" height="100" fill="#0d6a08" opacity=".18"/>
    <rect x="0" y="455" width="893" height="2" fill="#9ef58a" opacity=".8"/>
    <circle cx="467" cy="192" r="135" fill="#ffffff" opacity=".3"/>
  </svg>

  <p class="brand-back">HALCYON RIDGE<br>FUND</p>

  <div class="back-web">
    <p>barn@halcyonridgefund.example</p>
    <p>www.halcyonridgefund.example</p>
  </div>
</section>

</body>
</html>
```